Wild Harbor Realm Banner Ad

I Host a Server for Stoneforge. Its called Wild Harbor Realm.
I am looking for a catchy banner Ad that shows that we are clearly a Stoneforge server and we are fun for all ages. The server has plugins that adds different mechanics to the game, mechanics we have are listed on the picture added to this project.
If you don't know stone forge. I suggest you watch the video on Stoneforge.net. But the basis of the game is you can break blocks, mine ores, and build huge structures out of what you collect.
Our Current Website is www.wildharborrealm.com
And if you have Stoneforge and would like to see the basis of our server its mc.wildharborrealm.com.
Like i said i would like the logo to have a Stoneforge feel, and show who we are.
Thanks for you're time.
Reason: We do not need this project right away anymore, so more chances for submissions.
Thanks
Industry/Entity Type
Build
Logo Text
WHR or Wild Harbor Realm
Requirements
Must have
- Must have IP address mc.wildharborrealm.com
Nice to have
- Something to show we are Stoneforge related and have Economy so some sort of Money aspect. We are from Canada so if you can work that in too.
The size needed is 468x60 px

```html
<!DOCTYPE html>
<html lang="en">
<head>
<meta charset="utf-8">
<title>Wild Harbor Realm Banner Ad</title>
<link rel="stylesheet" href="https://fonts.googleapis.com/css2?family=Arvo:wght@700&family=Droid+Sans&family=Open+Sans:wght@400;600&display=swap">
<style>
  :root {
    --page-bg: #fbfde8;
    --sheet: #ffffff;
    --sheet-edge: #d6d8c4;
    --sheet-shadow: #a9ad90;
    --ink: #1a1a1a;
    --banner-gold: #f2bf28;
    --banner-grey: #d9d9d4;
    --banner-frame: #3a3a3a;
    --keyword: #8a8a86;
    --name: #4a3808;
    --table-head: #e9e9e9;
    --table-line: #d8d8d8;
    --row-bg: #ffffd9;
    --rank-green: #3f8f2f;
    --title-orange: #e38a00;
    --ip-green: #4a8a4a;
    --players-blue: #2a3fd0;
    --tag-bg: #4a4a4a;
    --tag-ink: #f2f2f2;
    --flag-red: #d52b1e;
  }
  * { box-sizing: border-box; margin: 0; padding: 0; }
  html, body { width: 1200px; height: 900px; overflow: hidden; }
  body { background: var(--page-bg); font-family: "Open Sans", sans-serif; color: var(--ink); position: relative; }

  .sheet-shadow { position: absolute; left: 27px; top: 27px; width: 1155px; height: 855px; background: var(--sheet-shadow); }
  .sheet { position: absolute; left: 15px; top: 15px; width: 1155px; height: 855px; background: var(--sheet); border: 1px solid var(--sheet-edge); }

  .sheet-title { position: absolute; left: 32px; top: 48px; font-size: 18px; text-decoration: underline; letter-spacing: 0.1px; }
  .size-label { position: absolute; font-size: 12px; text-decoration: underline; }
  .mockup-label { position: absolute; left: 175px; top: 435px; font-size: 12px; text-decoration: underline; }

  /* Banner, built at 780x100 */
  .banner { position: absolute; width: 780px; height: 100px; border: 3px solid var(--banner-frame); overflow: hidden; font-family: "Arvo", serif; font-weight: 700; }
  .banner-pattern { position: absolute; inset: 0; background: linear-gradient(180deg, var(--banner-gold) 0%, #f6cd4a 45%, var(--banner-grey) 100%); }
  .keyword { position: absolute; font-size: 16px; line-height: 1; color: var(--keyword); white-space: nowrap; }
  .banner-name { position: absolute; left: 8px; top: 42px; display: flex; align-items: baseline; color: var(--name); white-space: nowrap; line-height: 1; }
  .banner-name .prefix { font-size: 26px; }
  .banner-name .core { font-size: 50px; letter-spacing: 0.5px; }
  .banner-name .suffix { font-size: 22px; }

  .banner-small { transform: scale(0.6); transform-origin: 0 0; }
  .banner-slot { position: absolute; width: 468px; height: 60px; }

  /* Server list */
  .server-list { position: absolute; left: 140px; top: 465px; width: 881px; height: 235px; border: 1px solid var(--table-line); background: var(--row-bg); overflow: hidden; font-family: "Droid Sans", sans-serif; }
  .list-head { height: 33px; background: var(--table-head); border-bottom: 1px solid var(--table-line); position: relative; font-size: 15px; font-weight: 600; font-family: "Open Sans", sans-serif; color: #333; }
  .list-head span { position: absolute; top: 7px; }
  .col-divider { position: absolute; left: 712px; top: 33px; width: 1px; height: 200px; background: var(--table-line); }
  .rank-divider { position: absolute; left: 27px; top: 33px; width: 1px; height: 200px; background: var(--table-line); }
  .rank { position: absolute; left: 5px; top: 38px; font-size: 12px; font-weight: 700; color: var(--rank-green); }
  .flag { position: absolute; left: 5px; top: 54px; }
  .server-title { position: absolute; left: 30px; top: 36px; font-size: 19px; color: var(--title-orange); }
  .server-desc { position: absolute; left: 30px; top: 66px; width: 670px; font-size: 14px; line-height: 23px; color: #333; }
  .tags { position: absolute; left: 30px; top: 187px; display: flex; gap: 5px; }
  .tag { background: var(--tag-bg); color: var(--tag-ink); font-size: 11px; padding: 2px 5px; border-radius: 3px; border: 1px solid #222; line-height: 14px; }
  .ip-field { position: absolute; left: 30px; top: 212px; width: 440px; height: 24px; border: 1px solid #bbb; border-radius: 3px; background: #fff; display: flex; font-size: 14px; }
  .ip-field .ip-label { background: #e8e8e8; border-right: 1px solid #bbb; padding: 2px 5px; color: #444; }
  .ip-field .ip-value { padding: 2px 12px; }
  .ip-main { position: absolute; left: 746px; top: 58px; font-size: 14px; color: var(--ip-green); }
  .stats { position: absolute; left: 717px; top: 112px; font-size: 14px; line-height: 18px; color: #333; }
  .stats .players { color: var(--players-blue); }
</style>
</head>
<body>
  <div class="sheet-shadow"></div>
  <div class="sheet">
    <h1 class="sheet-title" style="font-weight:400">Wild Harbor Realm Banner Ad</h1>

    <div class="banner" style="left:190px; top:132px;">
      <div class="banner-pattern" role="img" aria-label="Yellow and grey block grid background"></div>
      <span class="keyword" style="left:33px; top:3px;">survival games</span>
      <span class="keyword" style="left:203px; top:3px;">mini-games</span>
      <span class="keyword" style="left:350px; top:2px;">hunger games</span>
      <span class="keyword" style="left:501px; top:2px;">monthly prizes and $$$</span>
      <span class="keyword" style="left:8px; top:20px;">towns</span>
      <span class="keyword" style="left:125px; top:19px;">epic ranks</span>
      <span class="keyword" style="left:271px; top:20px;">no griefing</span>
      <span class="keyword" style="left:410px; top:21px;">multiverse</span>
      <span class="keyword" style="left:586px; top:20px;">24/7</span>
      <span class="keyword" style="left:680px; top:19px;">mcskills</span>
      <div class="banner-name"><span class="prefix">mc.</span><span class="core">WildHarborRealm</span><span class="suffix">.com</span></div>
    </div>
    <span class="size-label" style="left:919px; top:241px;">780x100</span>

    <div class="banner-slot" style="left:347px; top:307px;">
      <div class="banner banner-small" style="left:0; top:0;">
        <div class="banner-pattern" role="img" aria-label="Yellow and grey block grid background"></div>
        <span class="keyword" style="left:33px; top:3px;">survival games</span>
        <span class="keyword" style="left:203px; top:3px;">mini-games</span>
        <span class="keyword" style="left:350px; top:2px;">hunger games</span>
        <span class="keyword" style="left:501px; top:2px;">monthly prizes and $$$</span>
        <span class="keyword" style="left:8px; top:20px;">towns</span>
        <span class="keyword" style="left:125px; top:19px;">epic ranks</span>
        <span class="keyword" style="left:271px; top:20px;">no griefing</span>
        <span class="keyword" style="left:410px; top:21px;">multiverse</span>
        <span class="keyword" style="left:586px; top:20px;">24/7</span>
        <span class="keyword" style="left:680px; top:19px;">mcskills</span>
        <div class="banner-name"><span class="prefix">mc.</span><span class="core">WildHarborRealm</span><span class="suffix">.com</span></div>
      </div>
    </div>
    <span class="size-label" style="left:771px; top:375px;">468x60</span>

    <span class="mockup-label">Stoneforge Server List Mock-up.</span>

    <div class="server-list">
      <div class="list-head">
        <span style="left:31px;">Server name &amp; Description</span>
        <span style="left:718px;">IP Address &amp; Port</span>
      </div>
      <div class="rank-divider"></div>
      <div class="col-divider"></div>
      <span class="rank">#1</span>
      <svg class="flag" width="16" height="11" viewBox="0 0 16 11" aria-hidden="true">
        <rect width="16" height="11" fill="#fff" stroke="#ccc"/>
        <rect width="4" height="11" fill="var(--flag-red)"/>
        <rect x="12" width="4" height="11" fill="var(--flag-red)"/>
        <rect x="6.5" y="3" width="3" height="5" fill="var(--flag-red)"/>
      </svg>
      <div class="server-title">Wild Harbor Realm -Hunger Games-</div>
      <p class="server-desc">1.4.5 This Server includes the following in Game material - HUGE ECONOMY - TOWNS - MCSKILLS - HUNGER GAMES !!!!!! - LOTTERY - VOTECASTER pay $300/vote and 16 Porkcops - DAILY GAME</p>

      <div class="banner-slot" style="left:29px; top:122px;">
        <div class="banner banner-small" style="left:0; top:0;">
          <div class="banner-pattern" role="img" aria-label="Yellow and grey block grid background"></div>
          <span class="keyword" style="left:33px; top:3px;">survival games</span>
          <span class="keyword" style="left:203px; top:3px;">mini-games</span>
          <span class="keyword" style="left:350px; top:2px;">hunger games</span>
          <span class="keyword" style="left:501px; top:2px;">monthly prizes and $$$</span>
          <span class="keyword" style="left:8px; top:20px;">towns</span>
          <span class="keyword" style="left:125px; top:19px;">epic ranks</span>
          <span class="keyword" style="left:271px; top:20px;">no griefing</span>
          <span class="keyword" style="left:410px; top:21px;">multiverse</span>
          <span class="keyword" style="left:586px; top:20px;">24/7</span>
          <span class="keyword" style="left:680px; top:19px;">mcskills</span>
          <div class="banner-name"><span class="prefix">mc.</span><span class="core">WildHarborRealm</span><span class="suffix">.com</span></div>
        </div>
      </div>

      <div class="tags">
        <span class="tag">Version: 1.4.5</span>
        <span class="tag">Survival</span>
        <span class="tag">Brickit</span>
        <span class="tag">Hunger Games</span>
        <span class="tag">McSkills</span>
        <span class="tag">No Whitelist</span>
        <span class="tag">PVE</span>
        <span class="tag">PVP</span>
        <span class="tag">Economy</span>
        <span class="tag">ClipTube Video</span>
      </div>
      <div class="ip-field"><span class="ip-label">Server IP Address</span><span class="ip-value">203.0.113.86</span></div>

      <span class="ip-main">203.0.113.86</span>
      <div class="stats">
        <div class="players">Players Online: 55 / 100</div>
        <div>1134 Votes in January</div>
        <div>4675 Votes - all time</div>
      </div>
    </div>
  </div>
</body>
</html>
```